Create a basic website for a new air cargo consultancy, called 'Veltrane Loadwise'

We want to build a basic website (homepage, 'about us' page, services and contact us page).
We have a logo, we have most of the text to be inserted, but not all. We also still need to take pictures.
We would like to have a fresh and modern, but business like design and the creation of the website.
We want to be able to modify the website after (add pictures and more text, update references).
We already have a url.

```html
<!DOCTYPE html>
<html lang="en">
<head>
<meta charset="utf-8">
<title>Veltrane Loadwise — Air Cargo Consultancy</title>
<link href="https://fonts.googleapis.com/css2?family=Tinos:wght@400;700&family=Mulish:wght@400;600;700;800&display=swap" rel="stylesheet">
<style>
:root{
  --navy:#2b3990;
  --navy-deep:#25307f;
  --gold:#d4a02a;
  --ink:#3b3d4a;
  --lavender:#eceefa;
  --white:#ffffff;
  --field:#f7f7fb;
}
*{box-sizing:border-box;margin:0;padding:0}
html,body{width:1200px;height:3976px;overflow:hidden}
body{position:relative;background:var(--white);font-family:"Mulish",sans-serif;color:var(--ink)}
.abs{position:absolute}
.serif{font-family:"Tinos",serif}

/* hero */
.hero{left:0;top:0;width:1200px;height:700px;
  background:linear-gradient(180deg,#e9eff6 0%,#cfdbe6 24%,#b7c5a8 34%,#aeb6b7 44%,#9aa4ac 70%,#b8bcc0 100%)}
.hero-plane{left:330px;top:270px;width:790px;height:300px;border-radius:200px 60px 120px 60px;
  background:linear-gradient(180deg,#2aa3c9 0%,#1a7fa9 70%,#c9b48a 100%);opacity:.9}
.hero-wave{left:0;top:590px;width:1200px;height:120px}
.brand{display:flex;align-items:center;gap:10px}
.brand-mark{width:16px;height:16px;border-radius:50%;background:var(--gold)}
.brand-name{font-family:"Tinos",serif;font-size:30px;color:var(--gold);letter-spacing:1px;line-height:1}
.brand-sub{font-size:8px;letter-spacing:3px;color:var(--navy);font-weight:700;margin-top:6px}
.header-brand{left:136px;top:44px}
.nav{left:426px;top:51px;display:flex;gap:26px;align-items:center;font-family:"Mulish",sans-serif;font-size:14px;font-weight:600;color:var(--navy)}
.nav a{color:var(--navy);text-decoration:none}
.nav .active{background:var(--gold);color:var(--white);padding:6px 10px;border-radius:4px}
.call{left:866px;top:38px;display:flex;gap:12px;align-items:center;color:var(--navy)}
.call small{display:block;font-size:14px;font-weight:600}
.call strong{display:block;font-size:19px;font-weight:800}
.hero-title{left:0;width:1200px;top:148px;text-align:center;font-size:56px;color:var(--navy);font-family:"Tinos",serif}
.hero-sub{left:0;width:1200px;top:218px;text-align:center;font-size:14px;color:#23263a;font-weight:600}

/* welcome */
.welcome-photo{left:133px;top:767px;width:451px;height:406px;border-radius:22px;
  background:linear-gradient(170deg,#0f6e93 0%,#3b9ec2 40%,#c6d3da 70%,#8d8f8d 100%)}
.welcome-head{left:636px;top:766px;font-size:31px;color:var(--navy);line-height:44px;font-family:"Tinos",serif}
.welcome-head b{font-weight:700}
.rule{height:2px;background:var(--gold)}
.welcome-text{left:637px;top:903px;width:435px;font-size:15px;line-height:24px;color:var(--ink)}
.welcome-text p+p{margin-top:30px}
.btn{display:inline-block;background:var(--gold);color:var(--white);font-weight:700;border-radius:22px;text-align:center;text-transform:uppercase}
.welcome-btn{left:637px;top:1134px;width:128px;height:42px;line-height:42px;font-size:14px}

/* features */
.features{left:120px;top:1254px;width:960px;height:136px;display:flex}
.feature{flex:1;text-align:center;padding-top:16px;border-left:2px solid var(--gold)}
.feature:first-child{border-left:none}
.feature svg{width:54px;height:54px;stroke:var(--navy);fill:none;stroke-width:2}
.feature span{display:block;margin-top:18px;font-family:"Tinos",serif;font-size:19px;color:var(--navy);letter-spacing:.3px}

/* services */
.services-bg{left:0;top:1440px;width:1200px;height:840px}
.services-plane{left:684px;top:1482px;width:516px;height:140px;border-radius:80px 0 0 80px;
  background:linear-gradient(90deg,#e8e9ee 0%,#c9ccd6 55%,#20336e 100%)}
.section-title{font-family:"Tinos",serif;font-weight:700;font-size:30px;color:var(--navy)}
.services-title{left:142px;top:1614px}
.services-sub{left:143px;top:1668px;font-size:22px;color:#2b2d3a}
.ghost{left:694px;top:1636px;font-family:"Tinos",serif;font-size:80px;color:transparent;-webkit-text-stroke:1.2px #c9cde8;letter-spacing:1px}
.card{top:1791px;width:224px;height:371px;border-radius:10px;overflow:hidden}
.card .label{position:absolute;left:30px;bottom:20px;font-family:"Tinos",serif;font-size:20px;line-height:24px;color:var(--white)}
.c1{left:137px;background:linear-gradient(180deg,#f0b35a 0%,#b07f47 40%,#5a4c43 70%,#1c1c22 100%)}
.c2{left:372px;background:linear-gradient(180deg,#e59c62 0%,#9aa0ab 40%,#6b5346 70%,#1c1c22 100%)}
.c3{left:610px;background:linear-gradient(180deg,#f0c586 0%,#b49363 40%,#6c5b40 70%,#1c1c22 100%)}
.c4{left:846px;background:linear-gradient(180deg,#bfa887 0%,#c9a45a 45%,#5a4a37 75%,#1c1c22 100%)}

/* blog */
.center{left:0;width:1200px;text-align:center}
.blog-title{top:2313px}
.blog-sub{top:2368px;font-size:22px;color:#2b2d3a}
.blog-card{top:2478px;width:298px;height:440px;background:var(--white);border-radius:10px;box-shadow:0 4px 18px rgba(40,50,110,.12);overflow:hidden}
.blog-card .thumb{height:207px}
.blog-card h3{margin:28px 32px 0;font-family:"Tinos",serif;font-weight:400;font-size:20px;line-height:26px;color:var(--navy)}
.blog-card p{margin:18px 32px 0;font-size:13px;line-height:19px;color:var(--ink)}
.blog-card .btn{margin:22px 0 0 32px;width:100px;height:30px;line-height:30px;font-size:11px}
.b1{left:133px}.b2{left:451px}.b3{left:767px}
.t1{background:linear-gradient(180deg,#2c4d7c 0%,#7d93ab 50%,#8b7c6a 100%)}
.t2{background:linear-gradient(180deg,#c9c7c1 0%,#a7a39a 55%,#7c7668 100%)}
.t3{background:linear-gradient(180deg,#a3abb9 0%,#8590a3 55%,#5f6a7c 100%)}

/* contact */
.contact-bg{left:0;top:2987px;width:1200px;height:760px;
  background:linear-gradient(180deg,#eceefa 0%,#f1f1f6 50%,#d9d2c8 70%,#c9b9a5 82%,#6e6b6a 100%)}
.contact-title{top:3026px}
.form-frame{left:262px;top:3134px;width:657px;height:363px;border:7px solid var(--white);border-bottom:none}
.field{background:var(--field);font-size:12px;color:#6b6d7a;padding:12px 18px;border:none}
.fn{left:313px;top:3181px;width:274px;height:41px}
.ln{left:604px;top:3181px;width:275px;height:41px}
.em{left:313px;top:3236px;width:274px;height:42px}
.ph{left:604px;top:3236px;width:275px;height:42px}
.msg{left:313px;top:3289px;width:566px;height:102px}
.submit{left:531px;top:3414px;width:113px;height:37px;line-height:37px;font-size:15px}
.contact-plane{left:120px;top:3470px;width:840px;height:160px;border-radius:100px 80px 60px 60px;
  background:linear-gradient(180deg,#e5e1da 0%,#c9c4bb 60%,#77736e 100%);opacity:.85}

/* footer */
.footer-wave{left:0;top:3620px;width:1200px;height:356px}
.footer-brand{left:139px;top:3760px}
.footer-brand .brand-name{font-size:40px}
.footer-brand .brand-sub{color:var(--gold);font-size:10px}
.fcol{top:3744px;color:var(--white)}
.fcol h4{font-size:12px;font-weight:800;letter-spacing:.3px;margin-bottom:16px}
.fcol li{list-style:none;font-size:13px;line-height:20px}
.menu{left:482px}
.contact-col{left:636px}
.contact-col li{display:flex;gap:12px;align-items:center;line-height:24px}
.contact-col svg{width:13px;height:13px;fill:var(--white)}
.follow{left:908px}
.socials{display:flex;gap:8px;margin-top:-2px}
.socials span{width:34px;height:34px;border-radius:50%;background:var(--white);display:block}
.foot-rule{left:136px;top:3900px;width:928px;height:1px;background:rgba(255,255,255,.18)}
.copyright{top:3926px;font-size:12px;color:var(--white)}
</style>
</head>
<body>

<!-- hero -->
<div class="abs hero" role="img" aria-label="Photo of a blue passenger jet at an airport stand with cargo trucks and loaders"></div>
<div class="abs hero-plane" role="img" aria-label="Blue airliner on the apron"></div>
<svg class="abs hero-wave" viewBox="0 0 1200 120" preserveAspectRatio="none"><path d="M0 40 C200 140 420 110 640 70 C860 30 1020 50 1200 80 L1200 120 L0 120 Z" fill="#ffffff"/></svg>

<div class="abs header-brand">
  <div class="brand"><span class="brand-mark"></span><span class="brand-name">VELTRANE</span></div>
  <div class="brand-sub">LOADWISE · MARTEN RALVE</div>
</div>
<nav class="abs nav">
  <a class="active" href="#">HOME</a><a href="#">ABOUT US</a><a href="#">SERVICES</a><a href="#">CONTACT US</a>
</nav>
<div class="abs call">
  <svg width="34" height="34" viewBox="0 0 24 24" fill="none" stroke="#2b3990" stroke-width="1.4"><path d="M5 3h4l2 5-2.5 1.5a11 11 0 0 0 6 6L16 13l5 2v4a2 2 0 0 1-2 2A16 16 0 0 1 3 5a2 2 0 0 1 2-2z"/><path d="M15 3a6 6 0 0 1 6 6M15 6.5a3 3 0 0 1 2.5 2.5"/></svg>
  <div><small>Call Us</small><strong>+1 555 014 2290</strong></div>
</div>
<h1 class="abs hero-title">VELTRANE LOADWISE</h1>
<p class="abs hero-sub">YOUR PREMIER CONSULTANCY SPECIALIZED IN THE AIR CARGO SECTOR</p>

<!-- welcome -->
<div class="abs welcome-photo" role="img" aria-label="Photo of a white cargo jet being loaded with pallets, with a gold plane silhouette above"></div>
<h2 class="abs welcome-head">WELCOME TO<br><b>VELTRANE LOADWISE</b></h2>
<div class="abs rule" style="left:636px;top:869px;width:88px"></div>
<div class="abs welcome-text">
  <p>Welcome to Veltrane Loadwise, your premier consultancy specialized in the air cargo sector. We are dedicated to helping clients enhance their overall cargo strategy, drive digital transformation, foster community building, and achieve sustainability goals.</p>
  <p>At Veltrane Loadwise, we understand the unique challenges and opportunities within the air cargo industry.</p>
</div>
<a class="abs btn welcome-btn">READ MORE</a>

<!-- features -->
<div class="abs features">
  <div class="feature">
    <svg viewBox="0 0 54 54"><rect x="6" y="8" width="36" height="26" rx="2"/><path d="M12 28v-6M18 28v-10M24 28v-8M30 28v-12"/><circle cx="38" cy="34" r="8"/><path d="M44 40l6 6"/><path d="M20 34v10M28 34v10M16 44h16"/></svg>
    <span>STRATEGIC PLANNING</span>
  </div>
  <div class="feature">
    <svg viewBox="0 0 54 54"><rect x="20" y="6" width="28" height="22" rx="2"/><path d="M30 28v6M26 34h8"/><rect x="27" y="11" width="10" height="12"/><ellipse cx="12" cy="36" rx="7" ry="3"/><path d="M5 36v8c0 2 14 2 14 0v-8M5 40c0 2 14 2 14 0"/><path d="M12 30v-8h8"/></svg>
    <span>DIGITALIZATION</span>
  </div>
  <div class="feature">
    <svg viewBox="0 0 54 54"><circle cx="27" cy="20" r="14"/><path d="M13 20h28M27 6c-8 8-8 20 0 28M27 6c8 8 8 20 0 28"/><circle cx="14" cy="42" r="3"/><circle cx="27" cy="42" r="3"/><circle cx="40" cy="42" r="3"/><path d="M9 50c1-3 9-3 10 0M22 50c1-3 9-3 10 0M35 50c1-3 9-3 10 0"/></svg>
    <span>COMMUNITY BUILDING</span>
  </div>
  <div class="feature">
    <svg viewBox="0 0 54 54"><circle cx="27" cy="24" r="15"/><path d="M18 14c4 2 6 6 4 10s2 6 6 5M32 10c-2 4 2 6 6 8"/><path d="M8 34c4 10 12 14 19 14s15-4 19-14"/><path d="M27 40c2-4 6-6 10-4-2 4-6 5-10 4z"/></svg>
    <span>SUSTAINABILITY</span>
  </div>
</div>

<!-- services -->
<svg class="abs services-bg" viewBox="0 0 1200 840" preserveAspectRatio="none"><defs><linearGradient id="svcTint" x1="0" y1="0" x2="0" y2="1"><stop offset="0" stop-color="#f3f4fb"/><stop offset=".25" stop-color="#eceefa"/><stop offset="1" stop-color="#eceefa"/></linearGradient></defs><path d="M0 0 C300 40 600 60 1200 20 L1200 828 L0 790 Z" fill="url(#svcTint)"/></svg>
<div class="abs services-plane" role="img" aria-label="Photo of a white and navy passenger jet in flight"></div>
<h2 class="abs section-title services-title">OUR SERVICES</h2>
<p class="abs services-sub">Air Freight Forwarding Services For Your Business</p>
<div class="abs rule" style="left:142px;top:1722px;width:50px"></div>
<div class="abs ghost">SERVICES</div>

<div class="abs card c1" role="img" aria-label="Photo of a yellow-tailed aircraft with wrapped cargo pallets"><div class="label">AIR FREIGHT<br>FORWARDING</div></div>
<div class="abs card c2" role="img" aria-label="Photo of an aircraft nose at sunset with ground vehicles"><div class="label">AVIATION<br>LOGISTICS</div></div>
<div class="abs card c3" role="img" aria-label="Photo of a ground worker beside cargo under an aircraft wing"><div class="label">COLD CHAIN<br>LOGISTICS</div></div>
<div class="abs card c4" role="img" aria-label="Photo of a forklift carrying stacked cargo boxes"><div class="label">CARGO CHARTER<br>FLIGHTS</div></div>

<!-- blog -->
<h2 class="abs center section-title blog-title">LATEST BLOG</h2>
<p class="abs center blog-sub">Lorem Ipsum is simply dummy text of the printing and typesetting</p>
<div class="abs rule" style="left:575px;top:2428px;width:50px"></div>

<article class="abs blog-card b1">
  <div class="thumb t1" role="img" aria-label="Photo of an airport cargo terminal at dusk"></div>
  <h3>Lorem Ipsum is simply dummy text of the.</h3>
  <p>Lorem ipsum dolor sit amet, consectetur adipiscing elit, sed do eiusmod tempor incididun.</p>
  <a class="btn">READ MORE</a>
</article>
<article class="abs blog-card b2">
  <div class="thumb t2" role="img" aria-label="Photo of an aircraft at a boarding bridge with loaders"></div>
  <h3>Lorem Ipsum is simply dummy text of the.</h3>
  <p>Lorem ipsum dolor sit amet, consectetur adipiscing elit, sed do eiusmod tempor incididun.</p>
  <a class="btn">READ MORE</a>
</article>
<article class="abs blog-card b3">
  <div class="thumb t3" role="img" aria-label="Photo of a private jet flying over misty mountains"></div>
  <h3>Lorem Ipsum is simply dummy text of the.</h3>
  <p>Lorem ipsum dolor sit amet, consectetur adipiscing elit, sed do eiusmod tempor incididun.</p>
  <a class="btn">READ MORE</a>
</article>

<!-- contact -->
<div class="abs contact-bg" role="img" aria-label="Photo of a white airliner parked on a snowy apron with mountains behind"></div>
<div class="abs contact-plane" role="img" aria-label="Parked white airliner with stairs and ground equipment"></div>
<h2 class="abs center section-title contact-title">CONTACT US</h2>
<div class="abs rule" style="left:575px;top:3089px;width:50px"></div>
<div class="abs form-frame"></div>
<div class="abs field fn">First Name</div>
<div class="abs field ln">Last Name</div>
<div class="abs field em">Email id</div>
<div class="abs field ph">Phone</div>
<div class="abs field msg">Message</div>
<a class="abs btn submit">SUBMIT</a>

<!-- footer -->
<svg class="abs footer-wave" viewBox="0 0 1200 356" preserveAspectRatio="none"><path d="M0 20 C260 70 520 70 760 40 C960 14 1100 0 1200 10 L1200 356 L0 356 Z" fill="#2b3990"/></svg>
<div class="abs footer-brand">
  <div class="brand"><span class="brand-mark"></span><span class="brand-name">VELTRANE</span></div>
  <div class="brand-sub">LOADWISE · MARTEN RALVE</div>
</div>
<div class="abs fcol menu">
  <h4>MENU</h4>
  <ul><li>HOME</li><li>ABOUT US</li><li>SERVICES</li><li>CONTACT US</li></ul>
</div>
<div class="abs fcol contact-col">
  <h4>CONTACT US</h4>
  <ul>
    <li><svg viewBox="0 0 24 24"><path d="M12 2a7 7 0 0 0-7 7c0 5 7 13 7 13s7-8 7-13a7 7 0 0 0-7-7zm0 9.5A2.5 2.5 0 1 1 12 6.5a2.5 2.5 0 0 1 0 5z"/></svg>USA</li>
    <li><svg viewBox="0 0 24 24"><path d="M6 2h4l2 5-3 2a11 11 0 0 0 6 6l2-3 5 2v4a2 2 0 0 1-2 2A17 17 0 0 1 4 4a2 2 0 0 1 2-2z"/></svg>+1 555 014 2290</li>
    <li><svg viewBox="0 0 24 24"><path d="M2 5h20v14H2z M2 5l10 8 10-8" /></svg>info@veltraneloadwise.com</li>
  </ul>
</div>
<div class="abs fcol follow">
  <h4>FOLLOW US</h4>
  <div class="socials" aria-label="Social media links"><span></span><span></span><span></span><span></span></div>
</div>
<div class="abs foot-rule"></div>
<p class="abs center copyright">Copyright © 2024 All Rights Reserved</p>

</body>
</html>
```